"Landing Page Design for Premium Eco-Friendly Laundry Strips – Plooifris.nl"

We need a visually appealing and high-converting landing page for our premium laundry strips, emphasizing luxury, sustainability, and ease of use. The page should include sections such as:

Hero Section: A compelling introduction with a strong headline, subheadline, and a clear call-to-action (CTA).
Product Benefits: Highlighting key features like eco-friendliness, long-lasting scent, and hypoallergenic qualities.
Product Description: Focusing on innovation and sustainability.
How It Works: Simple, visual steps for using the product.
Customer Reviews: Authentic testimonials to build trust and social proof.
FAQ Section: Addressing common concerns about the product.
The design should maintain a luxurious aesthetic while ensuring clarity and user-friendliness. We also offer free shipping on all orders, a key differentiator to be prominently displayed. All texts and translations are already provided for implementation. Please deliver the design in Figma format."

Target Market(s)

"Eco-conscious consumers and families seeking premium and sustainable laundry solutions. Target age group: 25-50, predominantly women who prioritize luxury and environmental impact."

Industry/Entity Type

"Laundry care and eco-friendly consumer goods."

Coding

Requirements
Must have
• A visually luxurious design emphasizing premium quality and eco-friendliness. Clear call-to-actions (e.g., 'Try Now – Free Shipping'). Sections for product benefits, how it works, customer reviews, and FAQ. Highlight free shipping with no minimum order prominently."
Nice to have
• Elegant, minimalist animations to enhance the premium feel. Subtle use of gold and black to emphasize luxury, with a touch of green for sustainability. Interactive customer reviews section (e.g., carousel or testimonials)."
Should not have
• Overly cluttered designs or overwhelming text blocks. Generic stock photos not aligned with our brand identity. Bright or overly playful color schemes that detract from the premium feel."

```html
<!DOCTYPE html>
<html lang="en">
<head>
<meta charset="utf-8">
<title>Plooifris.nl – Premium Laundry Strips</title>
<link href="https://fonts.googleapis.com/css2?family=Jost:ital,wght@0,400;0,500;0,600;0,700;1,400;1,500&display=swap" rel="stylesheet">
<style>
:root{
  --gold:#c48e2c;
  --gold-dark:#b07c1f;
  --gold-light:#e8c04e;
  --ink:#1f1f1f;
  --text:#3a3a3a;
  --muted:#7a7a7a;
  --cream:#fdf6e4;
  --footer:#1e1e1e;
  --white:#ffffff;
}
*{margin:0;padding:0;box-sizing:border-box}
html,body{width:1200px;height:3765px;overflow:hidden}
body{font-family:'Jost',sans-serif;color:var(--text);background:var(--white);position:relative}
.abs{position:absolute}
.center{text-align:center}

/* top bar */
.topbar{left:0;top:0;width:1200px;height:51px;background:var(--gold);color:var(--white);font-style:italic;font-weight:500;font-size:16px;line-height:51px;text-align:center;letter-spacing:.3px}

/* hero */
.hero-photo{left:0;top:51px;width:1200px;height:680px;background:linear-gradient(100deg,#ecebee 0%,#e4e3e6 40%,#d9d6d6 60%,#c9c3bd 100%)}
.hero-curves{left:0;top:0;width:1200px;height:760px}
.brand{display:flex;flex-direction:column;align-items:center;gap:8px}
.brand-dot{border-radius:50%;background:var(--gold)}
.brand-name{color:var(--gold);font-weight:500;letter-spacing:.5px}
.hero-brand{left:100px;top:84px;width:120px}
.hero-brand .brand-dot{width:56px;height:56px}
.hero-brand .brand-name{font-size:17px}
.nav{top:82px;font-size:20px;color:var(--ink)}
.nav.active{color:var(--gold)}
.btn{background:var(--gold-light);color:var(--ink);font-weight:600;border-radius:4px 16px 4px 16px;display:flex;align-items:center;justify-content:center}
.btn-ship{left:919px;top:73px;width:170px;height:41px;font-size:17px}
.hero-kicker{left:101px;top:266px;font-size:32px;color:var(--ink)}
.hero-title{left:100px;top:310px;font-size:48px;font-weight:700;color:var(--gold);letter-spacing:1.5px}
.hero-text{left:101px;top:374px;width:420px;font-size:19px;line-height:30px;color:var(--ink)}
.btn-try{left:101px;top:453px;width:120px;height:42px;font-size:17px}
.hero-note{left:101px;top:514px;font-size:14px;font-style:italic;color:var(--ink)}

/* benefits */
.benefit{top:804px;width:313px;height:215px;background:var(--white);border-radius:30px 4px 30px 4px;box-shadow:0 8px 30px rgba(0,0,0,.07);text-align:center;padding-top:76px}
.benefit.outlined{border:1.5px solid var(--gold-light);box-shadow:none}
.benefit h3{font-size:19px;font-weight:500;color:var(--ink)}
.benefit p{margin:14px auto 0;width:260px;font-size:14px;line-height:26px;color:var(--muted)}
.icon-disc{border-radius:50%;background:linear-gradient(145deg,var(--gold-light),var(--gold));display:flex;align-items:center;justify-content:center}
.benefit-icon{top:770px;width:88px;height:88px}

/* about */
.product-shot{left:117px;top:1093px;width:435px;height:668px;background:linear-gradient(150deg,#f1ede4 0%,#e7dcc2 30%,#1c1a16 45%,#111 80%,#caa043 100%);border-radius:6px;z-index:3;box-shadow:8px 10px 30px rgba(0,0,0,.25)}
.about-title{left:642px;top:1122px;font-size:35px;font-weight:700;color:var(--gold);letter-spacing:1px}
.about-text{left:642px;top:1176px;width:460px;font-size:16px;line-height:29px;color:var(--muted)}
.feature-icon{width:64px;height:64px;border-radius:50%;background:var(--white);box-shadow:0 4px 18px rgba(0,0,0,.09);display:flex;align-items:center;justify-content:center;left:642px}
.feature-title{left:729px;font-size:19px;font-weight:600;color:var(--gold)}
.feature-text{left:729px;width:360px;font-size:14px;line-height:25px;color:var(--muted)}
.btn-about{left:643px;top:1489px;width:118px;height:42px;font-size:17px}

/* how it works */
.how-bg{left:0;top:1560px;width:1200px;height:760px}
.how-title{left:0;top:1786px;width:1200px;font-size:35px;font-weight:700;color:var(--white);letter-spacing:1px}
.how-text{left:250px;top:1844px;width:700px;font-size:17px;line-height:28px;color:var(--white)}
.step{top:1932px;width:308px;height:291px;border:1.5px solid rgba(255,255,255,.85);border-radius:40px 4px 40px 4px;text-align:center;color:var(--white);padding-top:143px}
.step.solid{background:var(--white);color:var(--ink);border-color:var(--white)}
.step h3{font-size:16px;font-weight:600;letter-spacing:.4px}
.step p{margin:12px auto 0;width:260px;font-size:14px;line-height:27px}
.step-disc{top:1971px;width:85px;height:85px;border-radius:50%;background:var(--white);display:flex;align-items:center;justify-content:center}
.step-disc.gold{background:var(--gold)}
.step-num{top:1972px;width:30px;height:30px;border-radius:50%;background:var(--gold-light);color:var(--white);font-size:12px;font-weight:600;display:flex;align-items:center;justify-content:center}

/* faq */
.faq-title{left:0;top:2381px;width:1200px;font-size:35px;font-weight:700;color:var(--gold);letter-spacing:1px}
.faq-item{left:219px;width:762px;background:var(--white);box-shadow:0 4px 20px rgba(0,0,0,.07);display:flex;align-items:center;justify-content:space-between;padding:0 26px;font-size:15px;font-weight:600;color:var(--ink);letter-spacing:.3px}
.faq-toggle{width:18px;height:18px;border-radius:50%;background:var(--gold);display:flex;align-items:center;justify-content:center}
.faq-answer{left:246px;top:2526px;width:690px;font-size:14.5px;line-height:28px;color:var(--muted)}

/* reviews */
.reviews{left:0;top:2986px;width:1200px;height:383px;background:var(--cream)}
.reviews-title{left:0;top:3057px;width:1200px;font-size:35px;font-weight:700;color:var(--gold);letter-spacing:1px}
.review-text{left:240px;top:3120px;width:720px;font-size:16px;line-height:32px;color:var(--muted)}
.arrow{top:3162px;width:35px;height:35px;border-radius:50%;background:var(--gold);display:flex;align-items:center;justify-content:center}
.avatar{left:517px;top:3237px;width:54px;height:54px;border-radius:50%;background:linear-gradient(135deg,#cfd3d8,#8d949b)}
.reviewer{left:594px;top:3242px;font-size:16px;font-weight:500;color:var(--ink)}
.stars{left:592px;top:3266px;font-size:11px;color:var(--gold);letter-spacing:1px}

/* footer */
.footer{left:0;top:3369px;width:1200px;height:396px;background:var(--footer)}
.foot-brand{left:108px;top:3430px;width:200px}
.foot-brand .brand-dot{width:110px;height:110px}
.foot-brand .brand-name{font-size:30px;margin-top:14px}
.contact{top:3429px;width:240px;text-align:center;color:var(--white)}
.contact .icon-disc{width:56px;height:56px;margin:0 auto}
.contact .label{margin-top:18px;font-size:15px;font-weight:500}
.contact .value{margin-top:6px;font-size:22px;font-weight:500}
.foot-rule{left:406px;top:3581px;width:683px;height:1px;background:rgba(255,255,255,.25)}
.foot-nav{top:3606px;font-size:18px;color:var(--white)}
.social{top:3667px;width:32px;height:32px;border-radius:50%;background:var(--gold-light)}
.copyright{left:0;top:3718px;width:1200px;font-size:13px;color:var(--white)}
</style>
</head>
<body>

<div class="abs topbar">***&nbsp;&nbsp; FREE SHIPPING ON ALL ORDERS &nbsp;&nbsp;***</div>

<!-- hero -->
<div class="abs hero-photo" role="img" aria-label="Photo of a woman loading laundry into a front-loading washing machine"></div>
<svg class="abs hero-curves" viewBox="0 0 1200 760" aria-hidden="true">
  <defs>
    <linearGradient id="goldSweep" x1="0" y1="0" x2="1" y2="0">
      <stop offset="0" stop-color="#c48e2c"/>
      <stop offset=".6" stop-color="#d6a33a"/>
      <stop offset="1" stop-color="#e8c04e"/>
    </linearGradient>
  </defs>
  <path d="M0 560 C150 650 380 700 650 640 C850 595 1050 540 1200 560 L1200 760 L0 760 Z" fill="#ffffff"/>
  <path d="M40 612 C190 730 440 735 720 630 C880 570 990 525 1062 512 C960 525 830 565 680 615 C430 695 210 700 40 612 Z" fill="url(#goldSweep)"/>
</svg>

<div class="abs brand hero-brand"><span class="brand-dot"></span><span class="brand-name">PLOOIFRIS</span></div>
<div class="abs nav active" style="left:417px">Home</div>
<div class="abs nav" style="left:521px">Benefits</div>
<div class="abs nav" style="left:638px">How It Works</div>
<div class="abs nav" style="left:804px">Reviews</div>
<div class="abs btn btn-ship">Free Shipping</div>

<div class="abs hero-kicker">Say Goodbye to Messy Liquids</div>
<div class="abs hero-title">HELLO TO STRIPS</div>
<div class="abs hero-text">Sed ut perspiciatis unde omnis iste natus error sit voluptatem accusantium doloremque</div>
<div class="abs btn btn-try">Try Now</div>
<div class="abs hero-note">** Free shipping with no minimum order **</div>

<!-- benefits -->
<div class="abs benefit" style="left:111px"><h3>Eco-Friendliness</h3><p>Sed ut perspiciatis unde omnis iste natus error sit voluptatem accusantium doloremque laudantium</p></div>
<div class="abs benefit outlined" style="left:443px"><h3>Long-Lasting Scent</h3><p>Sed ut perspiciatis unde omnis iste natus error sit voluptatem accusantium doloremque laudantium</p></div>
<div class="abs benefit" style="left:775px"><h3>Hypoallergenic Qualities</h3><p>Sed ut perspiciatis unde omnis iste natus error sit voluptatem accusantium doloremque laudantium</p></div>

<div class="abs icon-disc benefit-icon" style="left:224px">
  <svg width="40" height="40" viewBox="0 0 40 40"><path d="M8 32 C8 16 20 8 34 8 C34 22 26 32 12 32 Z" fill="none" stroke="#fff" stroke-width="2.5"/><path d="M10 30 L26 16" stroke="#fff" stroke-width="2.5"/></svg>
</div>
<div class="abs icon-disc benefit-icon" style="left:556px">
  <svg width="40" height="40" viewBox="0 0 40 40"><rect x="11" y="16" width="18" height="19" rx="6" fill="#fff"/><rect x="16" y="10" width="8" height="6" fill="#fff"/><path d="M24 11 H31" stroke="#fff" stroke-width="2"/><circle cx="34" cy="8" r="1.5" fill="#fff"/></svg>
</div>
<div class="abs icon-disc benefit-icon" style="left:888px">
  <svg width="40" height="40" viewBox="0 0 40 40"><path d="M20 6 C26 14 30 19 30 25 A10 10 0 0 1 10 25 C10 19 14 14 20 6 Z" fill="none" stroke="#fff" stroke-width="2.5"/><path d="M15 25 L19 29 L26 21" fill="none" stroke="#fff" stroke-width="2.5"/></svg>
</div>

<!-- how it works background -->
<svg class="abs how-bg" viewBox="0 1560 1200 760" aria-hidden="true">
  <defs>
    <linearGradient id="howFill" x1="0" y1="0" x2="0" y2="1">
      <stop offset="0" stop-color="#c48e2c"/>
      <stop offset="1" stop-color="#b98427"/>
    </linearGradient>
  </defs>
  <path d="M0 1666 C300 1770 720 1730 1000 1630 C1100 1596 1160 1600 1200 1590 L1200 2320 L0 2320 Z" fill="url(#howFill)"/>
  <path d="M560 1712 C760 1660 960 1610 1160 1625 C1000 1630 820 1665 560 1712 Z" fill="#e8c04e"/>
</svg>

<!-- about -->
<div class="abs product-shot" role="img" aria-label="Product box of Plooistrips laundry strips in black and gold packaging"></div>
<div class="abs about-title">ABOUT PLOOISTRIPS</div>
<div class="abs about-text">Sed ut perspiciatis unde omnis iste natus error sit voluptatem accusantium doloremque laudantium, totam rem</div>

<div class="abs feature-icon" style="top:1260px">
  <svg width="30" height="30" viewBox="0 0 30 30"><path d="M10 5 L5 9 L8 13 L10 12 V25 H20 V12 L22 13 L25 9 L20 5 C18 8 12 8 10 5 Z" fill="none" stroke="#e8c04e" stroke-width="1.6"/></svg>
</div>
<div class="abs feature-title" style="top:1257px">Powerful Clean:</div>
<div class="abs feature-text" style="top:1289px">Ut enim ad minima veniam, quis nostrum exercitat ion em ullam corporis suscipit laboriosam, nisi ut</div>

<div class="abs feature-icon" style="top:1374px">
  <svg width="30" height="30" viewBox="0 0 30 30"><path d="M5 25 H25 L21 15 H9 Z" fill="none" stroke="#e8c04e" stroke-width="1.6"/><path d="M15 15 V6 M12 9 L15 6 L18 9" fill="none" stroke="#e8c04e" stroke-width="1.6"/></svg>
</div>
<div class="abs feature-title" style="top:1371px">Gentle on Skin:</div>
<div class="abs feature-text" style="top:1403px">Ut enim ad minima veniam, quis nostrum exercitat ion em ullam corporis suscipit laboriosam, nisi ut</div>

<div class="abs btn btn-about">Try Now</div>

<!-- how it works -->
<div class="abs how-title center">HOW IT WORKS</div>
<div class="abs how-text center">Ut enim ad minima veniam, quis nostrum exercitationem ullam corporis suscipit laboriosam, nisi ut aliquid ex ea commodi consequatur?</div>

<div class="abs step" style="left:111px"><h3>ULTRA-CONCENTRATED FORMULA</h3><p>The strips are made from plant-based, biodegradable ingredients, ensuring a gentle yet thorough clean.</p></div>
<div class="abs step solid" style="left:446px"><h3>DISSOLVES INSTANTLY</h3><p>Here's no need to worry about measuring or pouring messy liquids—just one strip per load.</p></div>
<div class="abs step" style="left:781px"><h3>ECO-FRIENDLY &amp; WASTE-FREE</h3><p>They are packaged in recyclable, compostable material to further reduce waste.</p></div>

<div class="abs step-disc" style="left:223px">
  <svg width="40" height="40" viewBox="0 0 40 40"><rect x="10" y="8" width="18" height="24" rx="2" fill="none" stroke="#e8c04e" stroke-width="2" transform="rotate(-12 19 20)"/><path d="M14 28 L30 12" stroke="#e8c04e" stroke-width="2"/></svg>
</div>
<div class="abs step-disc gold" style="left:558px">
  <svg width="40" height="40" viewBox="0 0 40 40"><path d="M12 8 H26 L30 12 V32 H12 Z" fill="none" stroke="#fff" stroke-width="2"/><circle cx="18" cy="20" r="1.5" fill="#fff"/><circle cx="23" cy="24" r="1.5" fill="#fff"/><circle cx="18" cy="27" r="1.5" fill="#fff"/></svg>
</div>
<div class="abs step-disc" style="left:893px">
  <svg width="40" height="40" viewBox="0 0 40 40"><path d="M14 7 L7 12 L11 18 L13 17 V33 H27 V17 L29 18 L33 12 L26 7 C24 11 16 11 14 7 Z" fill="none" stroke="#e8c04e" stroke-width="2"/></svg>
</div>
<div class="abs step-num" style="left:222px">01</div>
<div class="abs step-num" style="left:558px">02</div>
<div class="abs step-num" style="left:893px">03</div>

<!-- faq -->
<div class="abs faq-title center">FREQUENTLY ASKED QUESTIONS</div>
<div class="abs faq-item" style="top:2457px;height:47px">1. WHAT ARE LAUNDRY STRIPS?<span class="faq-toggle"><svg width="10" height="10" viewBox="0 0 10 10"><path d="M2 6 L5 3 L8 6" fill="none" stroke="#fff" stroke-width="1.6"/></svg></span></div>
<div class="abs faq-answer">Laundry strips are ultra-concentrated, eco-friendly detergent sheets that dissolve in water. They provide a mess-free, convenient alternative to traditional liquid or powder detergents, giving you a powerful clean while reducing packaging waste.</div>
<div class="abs faq-item" style="top:2638px;height:47px">2. HOW DO I USE LAUNDRY STRIPS?<span class="faq-toggle"><svg width="10" height="10" viewBox="0 0 10 10"><path d="M2 4 L5 7 L8 4" fill="none" stroke="#fff" stroke-width="1.6"/></svg></span></div>
<div class="abs faq-item" style="top:2711px;height:47px">3. ARE LAUNDRY STRIPS SUITABLE FOR ALL WASHING MACHINES?<span class="faq-toggle"><svg width="10" height="10" viewBox="0 0 10 10"><path d="M2 4 L5 7 L8 4" fill="none" stroke="#fff" stroke-width="1.6"/></svg></span></div>
<div class="abs faq-item" style="top:2784px;height:47px">4. HOW MANY STRIPS DO I NEED TO USE FOR EACH LOAD?<span class="faq-toggle"><svg width="10" height="10" viewBox="0 0 10 10"><path d="M2 4 L5 7 L8 4" fill="none" stroke="#fff" stroke-width="1.6"/></svg></span></div>
<div class="abs faq-item" style="top:2857px;height:50px">5. ARE LAUNDRY STRIPS SAFE FOR SENSITIVE SKIN?<span class="faq-toggle"><svg width="10" height="10" viewBox="0 0 10 10"><path d="M2 4 L5 7 L8 4" fill="none" stroke="#fff" stroke-width="1.6"/></svg></span></div>

<!-- reviews -->
<div class="abs reviews"></div>
<div class="abs reviews-title center">OUR HAPPY CUSTOMERS</div>
<div class="abs review-text center">Sed ut perspiciatis unde omnis iste natus error sit voluptatem accusantium doloremque laudan totam rem aperiam, eaque ipsa quae ab illo inventore veritatis et quasi architecto beatae vitae dicta sunt explicabo. Nemo enim ipsam voluptatem quia voluptas sit aspernatur</div>
<div class="abs arrow" style="left:154px"><svg width="12" height="12" viewBox="0 0 12 12"><path d="M6 3 L3 6 L6 9 M9 3 L6 6 L9 9" fill="none" stroke="#fff" stroke-width="1.4"/></svg></div>
<div class="abs arrow" style="left:1012px"><svg width="12" height="12" viewBox="0 0 12 12"><path d="M3 3 L6 6 L3 9 M6 3 L9 6 L6 9" fill="none" stroke="#fff" stroke-width="1.4"/></svg></div>
<div class="abs avatar" role="img" aria-label="Customer portrait photo"></div>
<div class="abs reviewer">Marieke Jansen</div>
<div class="abs stars">★★★★☆</div>

<!-- footer -->
<div class="abs footer"></div>
<div class="abs brand foot-brand"><span class="brand-dot"></span><span class="brand-name">PLOOIFRIS</span></div>

<div class="abs contact" style="left:373px">
  <div class="icon-disc"><svg width="22" height="22" viewBox="0 0 24 24"><path d="M6 3 L9 3 L10.5 8 L8.5 9.5 C9.5 11.8 12.2 14.5 14.5 15.5 L16 13.5 L21 15 L21 18 C21 19.7 19.7 21 18 21 C10 21 3 14 3 6 C3 4.3 4.3 3 6 3 Z" fill="#1e1e1e"/></svg></div>
  <div class="label">Contact Number</div>
  <div class="value">+31 20 555 0142</div>
</div>
<div class="abs contact" style="left:624px">
  <div class="icon-disc"><svg width="22" height="22" viewBox="0 0 24 24"><rect x="3" y="6" width="18" height="13" rx="2" fill="#1e1e1e"/><path d="M3.5 7 L12 13 L20.5 7" fill="none" stroke="#e8c04e" stroke-width="1.5"/></svg></div>
  <div class="label">Email Address</div>
  <div class="value">info@plooifris.nl</div>
</div>
<div class="abs contact" style="left:877px">
  <div class="icon-disc"><svg width="22" height="22" viewBox="0 0 24 24"><circle cx="12" cy="12" r="9" fill="#1e1e1e"/><path d="M3 12 H21 M12 3 C8 7 8 17 12 21 C16 17 16 7 12 3" fill="none" stroke="#e8c04e" stroke-width="1.4"/></svg></div>
  <div class="label">Website</div>
  <div class="value">www.plooifris.nl</div>
</div>

<div class="abs foot-rule"></div>
<div class="abs foot-nav" style="left:497px">Home</div>
<div class="abs foot-nav" style="left:602px">Benefits</div>
<div class="abs foot-nav" style="left:720px">How It Works</div>
<div class="abs foot-nav" style="left:884px">Reviews</div>
<div class="abs foot-nav" style="left:1003px">Contact Us</div>

<div class="abs social" style="left:514px"></div>
<div class="abs social" style="left:558px"></div>
<div class="abs social" style="left:604px"></div>
<div class="abs social" style="left:649px"></div>

<div class="abs copyright center">(C) Copyright 2024 | All Rights Reserved</div>

</body>
</html>
```